Need a new logo/business card for a cafe

I need a new logo and business card for a café. The café is called "Ladle", and we have a reputation for making a high quality cup of espresso coffee. I would like the business card design to reflect this "high quality". Our baristas craft our customers coffee with care to achieve this result. I would like to see designs that include a warm latte brown color. The card will be single sided to allow the rear to be used as a loyalty card which means the design will need to include space for our business address, phone number, and facebook page details. The uploaded logo is already in use on the café front window, and if it can be incorporated or used that would be great, but I am open to completely new designs as well. Thank you.
Updates
Thank you to all for the submissions. There's quite a few I like now, the hardest part will be choosing! I've set up a poll for added feedback from my own contacts and will wait on results from that.
Hello, more great designs coming in, thank you very much. There's quite a few that I really like, so my biggest challenge is going to be choosing one. Thanks again for your time, and I'll get onto the hard task of making that choice. Marisa
Industry/Entity Type
Cafe
Look and feel
Each slider illustrates characteristics of the customer's brand and the style your logo design should communicate.

```html
<!DOCTYPE html>
<html lang="en">
<head>
<meta charset="utf-8">
<title>Ladle Café – Business Card</title>
<link rel="stylesheet" href="https://fonts.googleapis.com/css2?family=Crimson+Text:wght@400;600&family=Great+Vibes&family=Montserrat:wght@400&display=swap">
<style>
  :root {
    --backdrop: #d9d6d3;
    --espresso: #3a3532;
    --latte: #8b7769;
    --mocha: #6f5f55;
    --roast: #564940;
    --cream: #ffffff;
  }
  * { margin: 0; padding: 0; box-sizing: border-box; }
  html, body {
    width: 1200px;
    height: 845px;
    overflow: hidden;
    background: var(--backdrop);
  }
  .canvas {
    position: relative;
    width: 1200px;
    height: 845px;
  }
  .business-card {
    position: absolute;
    left: 60px;
    top: 114px;
    width: 1080px;
    height: 617px;
    background: var(--espresso);
    overflow: hidden;
    box-shadow: 0 6px 24px rgba(0,0,0,0.25);
  }
  .card-waves {
    position: absolute;
    inset: 0;
    width: 100%;
    height: 100%;
  }
  .wave-roast { fill: var(--roast); }
  .wave-mocha { fill: var(--mocha); }
  .wave-latte { fill: var(--latte); }

  .brand {
    position: absolute;
    left: 400px;
    top: 95px;
    color: var(--cream);
    font-family: "Crimson Text", Georgia, serif;
    font-weight: 400;
  }
  .brand-name {
    display: block;
    font-size: 124px;
    line-height: 1;
  }
  .brand-tag {
    position: absolute;
    left: 258px;
    top: 128px;
    font-size: 30px;
    letter-spacing: 4px;
  }

  .contact {
    position: absolute;
    left: 600px;
    top: 372px;
    color: var(--cream);
    font-family: "Crimson Text", Georgia, serif;
    font-size: 23px;
    line-height: 1.45;
  }
  .contact-address { margin-bottom: 36px; }

  .staff {
    position: absolute;
    left: 120px;
    top: 418px;
    color: var(--cream);
    text-align: center;
  }
  .staff-name {
    display: block;
    font-family: "Great Vibes", cursive;
    font-size: 58px;
    line-height: 1;
  }
  .staff-role {
    display: block;
    margin-top: 2px;
    font-family: "Montserrat", Arial, sans-serif;
    font-size: 17px;
    letter-spacing: 7px;
  }
</style>
</head>
<body>
<main class="canvas">
  <section class="business-card">
    <svg class="card-waves" viewBox="0 0 1080 617" aria-hidden="true">
      <path class="wave-roast" d="M140 0 L1080 0 L1080 300 C900 330 700 360 520 420 C360 475 210 450 130 350 C50 250 60 90 140 0 Z"/>
      <path class="wave-mocha" d="M170 0 L1080 0 L1080 285 C900 315 700 345 520 405 C370 455 230 435 150 340 C75 250 90 85 170 0 Z"/>
      <path class="wave-latte" d="M205 0 L1080 0 L1080 270 C900 300 700 330 520 390 C380 440 250 420 175 330 C105 245 120 80 205 0 Z"/>
    </svg>

    <div class="brand">
      <span class="brand-name">Ladle</span>
      <span class="brand-tag">café</span>
    </div>

    <div class="staff">
      <span class="staff-name">Marisa Hart</span>
      <span class="staff-role">MANAGER</span>
    </div>

    <address class="contact" style="font-style: normal;">
      <p class="contact-address">4/112 Shore Road<br>Cooksby NSW 2590</p>
      <p class="contact-phone">Phone: (02) 4381 7620</p>
      <p class="contact-social">Facebook: cafeatcooksby</p>
    </address>
  </section>
</main>
</body>
</html>
```